Improve My Resume Design to be easier for the reader and the recruiter

I need to improve my resume design to make it easier to read and attract employer eyes in a very professional way. And the graphs should be neat, nice and professional. - You can use the below logos as the companies that I worked with are so famous.

Detailed information about me is inside the CV.

Target Market(s)

Big Companies and Famous recruiters

Industry/Entity Type

Government

Colors

Designer to choose colors to be used in the design.

Requirements
Must have
• Infographics .. Easy to Read.
Nice to have
• Charts, infographics.
Should not have
• not professional colours.

```html
<!DOCTYPE html>
<html lang="en">
<head>
<meta charset="utf-8">
<title>Karim Nabil Haddad — Resume</title>
<link href="https://fonts.googleapis.com/css2?family=Didact+Gothic&family=Montserrat:wght@400;600;700&display=swap" rel="stylesheet">
<style>
:root{
  --backdrop:#1f2940;
  --paper-shade:#e6e6e6;
  --sidebar:#e2e2e2;
  --sidebar-deep:#d9d9d9;
  --mint:#bfdbd8;
  --teal:#106e63;
  --teal-dark:#0d5b52;
  --ink:#3d3d3d;
  --ink-soft:#555;
  --heading:#24434a;
  --bar-dark:#4a4a4a;
  --strip:#333;
}
*{margin:0;padding:0;box-sizing:border-box}
html,body{width:1200px;height:741px;overflow:hidden}
body{background:var(--backdrop);font-family:"Didact Gothic",sans-serif;color:var(--ink);position:relative}
.page{position:absolute;top:92px;height:561px;background:linear-gradient(180deg,#f7f7f7,var(--paper-shade));overflow:hidden}
.page--one{left:147px;width:402px}
.page--two{left:599px;width:393px}
.abs{position:absolute}
.section-title{font-family:"Montserrat",sans-serif;font-weight:600;font-variant:small-caps;font-size:8.5px;letter-spacing:1px;color:var(--heading);text-decoration:underline;text-underline-offset:2px;text-decoration-thickness:1px;white-space:nowrap}
.body-text{font-size:6.9px;line-height:7.4px;text-align:justify;color:var(--ink-soft)}

/* page one */
.sidebar{left:20px;top:0;width:152px;height:561px;background:linear-gradient(180deg,#ececec,var(--sidebar))}
.photo{left:28px;top:25px;width:122px;height:131px;background:radial-gradient(ellipse at 45% 55%,#4a4a4a 0%,#8a8a8a 45%,#c9c9c9 100%)}
.strip-left{left:0;top:142px;width:20px;height:22px;background:var(--strip)}
.contact-band{left:172px;top:142px;width:230px;height:22px;background:var(--teal);color:#e8f3f1;font-size:6.6px;letter-spacing:.3px;display:flex;align-items:center;gap:6px;padding-left:12px;white-space:nowrap}
.contact-band span{display:flex;align-items:center;gap:2px}
.competency-panel{left:20px;top:157px;width:152px;height:201px;background:var(--mint)}
.name{left:185px;top:29px;font-family:"Montserrat",sans-serif;font-weight:700;font-size:7.6px;letter-spacing:.4px;color:var(--teal-dark)}
.job-title{left:185px;top:40px;font-size:6.8px;color:var(--teal)}
.date{right:22px;top:30px;font-size:6.8px;letter-spacing:.6px;color:var(--ink)}
.intro{left:185px;top:55px;width:195px}
.competencies{left:40px;top:196px;list-style:none;font-size:6.9px;color:var(--ink)}
.competencies li{height:13.35px}
.summary{left:185px;top:196px;width:195px;list-style:none;line-height:7.8px}
.summary li{margin-bottom:6px;position:relative}
.summary li::before{content:"";display:inline-block;width:3px;height:3px;background:#444;box-shadow:1px 1px 0 #bbb;margin:0 18px 1px 7px;vertical-align:middle}
.employer-logo{display:flex;align-items:center;gap:4px;font-size:7px;color:var(--ink);white-space:nowrap}
.mark{width:9px;height:9px;background:#c0782e;flex:none}
.mark--round{border-radius:50%;background:var(--teal)}
.mark--dark{background:#222}

/* page two */
.strip-left-two{left:0;top:47px;width:19px;height:22px;background:var(--strip)}
.header-mid{left:19px;top:47px;width:149px;height:22px;background:#e4e4e4}
.header-bar{left:168px;top:47px;width:225px;height:22px;background:var(--bar-dark)}
.sidebar-two{left:19px;top:69px;width:149px;height:492px;background:linear-gradient(180deg,#e6e6e6,var(--sidebar-deep))}
.logo-box{left:19px;top:69px;width:149px;height:68px;background:#dedede;display:flex;align-items:center;justify-content:center}
.logo-box--mint{top:364px;height:66px;background:var(--mint);flex-direction:column;gap:4px}
.divider{left:19px;top:363px;width:353px;border-top:1px dashed #888}
.company{left:28px;width:135px;font-size:6.8px;line-height:8px;color:var(--ink);text-transform:uppercase}
.role{left:28px;width:136px;font-size:6.1px;line-height:8px;color:var(--ink-soft)}
.duties{left:181px;width:190px;line-height:7.9px}
.duties p{text-indent:24px;margin-bottom:8.2px}
</style>
</head>
<body>

<section class="page page--one" aria-label="Resume page one">
  <div class="abs sidebar"></div>
  <div class="abs photo" role="img" aria-label="Portrait photograph of the candidate"></div>
  <div class="abs strip-left"></div>
  <div class="abs competency-panel"></div>

  <h1 class="abs name">KARIM NABIL HADDAD</h1>
  <p class="abs job-title">SENIOR PROJECT MANAGER</p>
  <p class="abs date">9.27.2019</p>
  <p class="abs intro body-text">Dedicated and multi-faceted professional with advanced analytical, reasoning and problem-solving skills, and offering over 13 years’ insightful experience performing investigative research and analysis to address tactical and strategic business challenges. Adept in the field of Project Management since 6 years with core skills in managing IT &amp; Non-IT Projects, CST Projects etc. Seeking an opportunity to leverage excellent project management, business analysis and data analytics skills and experience with a reputed organization to contribute to strategic business planning</p>

  <div class="abs contact-band">
    <span><svg width="6" height="8" viewBox="0 0 6 8"><path d="M3 0a3 3 0 0 0-3 3c0 2 3 5 3 5s3-3 3-5a3 3 0 0 0-3-3zm0 4.2a1.2 1.2 0 1 1 0-2.4 1.2 1.2 0 0 1 0 2.4z" fill="#e8f3f1"/></svg>Dubai, UAE</span>
    <span><svg width="7" height="7" viewBox="0 0 7 7"><path d="M1.4 0.3l1.1 1.4-.6.8c.4.9 1.1 1.6 2 2l.8-.6 1.4 1.1-.7 1.2C3 6 1 4 .2 1z" fill="#e8f3f1"/></svg>+971 555012347</span>
    <span>@k.haddad84@mailhub.com</span>
  </div>

  <h2 class="abs section-title" style="left:28px;top:173px">Core Competencies</h2>
  <ul class="abs competencies">
    <li>Leadership &amp; Team Building</li>
    <li>Business/IT Analysis</li>
    <li>Requirements Gathering/Analysis</li>
    <li>Business Consulting</li>
    <li>Project Management</li>
    <li>Issues And Crisis Management</li>
    <li>Business Process Re-engineering</li>
    <li>System/Services Support</li>
    <li>Client / Stakeholder Management</li>
    <li>Event Management</li>
    <li>Reporting &amp; Documentation</li>
    <li>Business Process Mapping</li>
  </ul>

  <h2 class="abs section-title" style="left:185px;top:173px">Profile Summary</h2>
  <ul class="abs summary body-text">
    <li>Hands-on exposure in handling all phases of Project Cycle, right from requirement analysis, project scoping, planning &amp; scheduling to the implementation of robust technology solutions within time, budget and quality.</li>
    <li>Proven ability to analyze requirements and the associated systems/applications to further translate business requirements into functional requirements</li>
    <li>Visionary leader, noted for sound, practical management style, and ability to lead high-performing technical and non-technical teams in various departments. Strong track record of developing top talent.</li>
    <li>Extensive experience serving as a liaison between business users and technical team to elicit, analyze, communicate, and validate requirements to understand business problems and opportunities in the context of requirements and recommend solutions that enable the organization to achieve its goals.</li>
    <li>Expert in furnishing business insights and analytics used to advance opportunity identification, process reengineering and facilitate corporate growth.</li>
    <li>Strong analytical and problem-solving skills coupled with thoroughness and attention to detail</li>
    <li>Skilled collaborator comfortable working across key functional business areas to deploy analytical insights around different functions.</li>
    <li>Adaptability of working independently as well as within cross-functional teams sharing common goals and objectives.</li>
    <li>Exceptional problem solver, with a logical, analytical and creative approach to problem-solving and a meticulous and organized approach to work.</li>
  </ul>

  <h2 class="abs section-title" style="left:28px;top:368px">Professional Experience</h2>
  <div class="abs employer-logo" style="left:46px;top:402px"><span class="mark"></span>Coastal City Council</div>
  <div class="abs employer-logo" style="left:36px;top:439px"><span class="mark mark--dark"></span>National Civil Service Authority</div>
  <div class="abs employer-logo" style="left:50px;top:479px"><span class="mark mark--round"></span>Tarnvale Petroleum</div>
</section>

<section class="page page--two" aria-label="Resume page two">
  <div class="abs strip-left-two"></div>
  <div class="abs header-mid"></div>
  <div class="abs header-bar"></div>
  <h2 class="abs section-title" style="left:28px;top:53px;color:#333">Professional Experience</h2>
  <div class="abs sidebar-two"></div>

  <div class="abs logo-box"><div class="employer-logo"><span class="mark mark--dark"></span>National Civil Service Authority</div></div>
  <p class="abs company" style="top:149px">National Civil Service Authority (NCSA), Dubai, UAE (Mar 2017 – Present)</p>
  <p class="abs role" style="top:183px">Senior Consultant - Human Resources Systems (Project Management Office)</p>

  <h2 class="abs section-title" style="left:181px;top:85px;color:var(--teal-dark)">Responsibilities</h2>
  <div class="abs duties body-text" style="top:103px">
    <p>Manage departmental plans and projects related to the HR Management Information Systems (HRMIS) and Services for Federal Ministries and autonomous authorities such as National Civil Service Authority (NCSA) Smart App, Enterprise Project Management System (EPM), Enterprise Strategic, Business Intelligent (BI), Halden Service Desk, to serve more than 60,000 federal government employees.</p>
    <p>Collate, document, review and analyze client business requirements and advice clients on the adoption of industry-wide practices.</p>
    <p>Ensure that business requirements are effectively translated into detailed functional and technical specifications from which appropriate business systems can be implemented or existing systems enhanced.</p>
    <p>Lead, identify, communicate and advance internal process improvement suggestions/ initiatives.</p>
    <p>Evaluate business processes, anticipate requirements, uncover areas for improvement, and develop and implement solutions.</p>
    <p>Serve as the liaison between business units, technology teams and support teams; render support in implementation and maintenance of business application systems.</p>
    <p>Consistently focus on maintaining established client satisfaction rating for the services provided.</p>
  </div>

  <div class="abs divider"></div>

  <div class="abs logo-box logo-box--mint"><span class="mark mark--round" style="width:18px;height:18px"></span><span class="employer-logo" style="font-weight:700">TARNVALE</span></div>
  <p class="abs company" style="top:440px">Tarnvale Upstream Holding B.V., Dubai, UAE (Dec 2011 - Feb 2017)</p>
  <p class="abs role" style="top:467px">Head – Corporate Affairs (Dec 2012 - Feb 2017) Executive - Performance &amp; Reporting, Business Planning &amp; Commercial Dept., Planning Unit (Dec 2011 – Dec 2012)</p>

  <h2 class="abs section-title" style="left:181px;top:381px;color:var(--teal-dark)">Highlight</h2>
  <div class="abs duties body-text" style="top:399px">
    <p>Lead the Corporate Communications department to assure strong brand positioning through internal and external Stakeholders Management and Corporate Social Responsibility programs and raise the company’s visibility in the Middle East region marketplace and manages its reputation amongst its key stakeholders using an integrated communication strategy.</p>
    <p>Successfully managed CSR projects related to the Corporate Affairs to develop the local communicates in the southern areas of Iraq with over USD 10 million allocated budget every year.</p>
  </div>
</section>

</body>
</html>
```